Tallow Crest Business Card

We need a business card designed for a a company called "Tallow Crest". We offer consulting, coaching and training to business leaders and coaches (across the world) using the latest findings in neuroscience, social and emotional intelligence and positive psychology. The final design should communicate the use of brain science to create sustainable relationships.

The card should be doublesided. The logo is attached and names and titles will be provided to the successful designer. Thank you.

Industry/Entity Type

Training

```html
<!DOCTYPE html>
<html lang="en">
<head>
<meta charset="utf-8">
<title>Tallow Crest Business Card</title>
<link href="https://fonts.googleapis.com/css2?family=Open+Sans:wght@400;700&display=swap" rel="stylesheet">
<style>
  :root {
    --page: #eeeeee;
    --card: #0c0c0c;
    --land-light: #3a3a3a;
    --land-dark: #1c1c1c;
    --brand-blue: #1d8fc4;
    --panel-blue: #1b8cc2;
    --lime: #a6c53a;
    --white: #ffffff;
  }
  * { margin: 0; padding: 0; box-sizing: border-box; }
  html, body {
    width: 1200px;
    height: 799px;
    overflow: hidden;
    background: var(--page);
    font-family: "Open Sans", sans-serif;
  }
  .card {
    position: absolute;
    left: 120px;
    top: 125px;
    width: 960px;
    height: 549px;
    background: var(--card);
    overflow: hidden;
  }
  .world-map {
    position: absolute;
    left: 30px;
    top: 20px;
    width: 900px;
    height: 380px;
    border-radius: 40px;
    background: radial-gradient(ellipse at center, var(--land-light) 0%, var(--land-dark) 65%, var(--card) 100%);
    opacity: 0.85;
  }
  .brand-name {
    position: absolute;
    left: 0;
    right: 0;
    top: 130px;
    text-align: center;
    color: var(--brand-blue);
    font-weight: 700;
    font-size: 58px;
    letter-spacing: 2px;
  }
  .brand-web {
    position: absolute;
    left: 0;
    right: 0;
    top: 240px;
    text-align: center;
    color: var(--lime);
    font-size: 26px;
    letter-spacing: 5px;
  }
  .contact-panel {
    position: absolute;
    left: 150px;
    right: 24px;
    top: 300px;
    bottom: -40px;
    background: var(--panel-blue);
    border: 3px solid var(--lime);
    border-radius: 70px 70px 0 0;
    color: var(--white);
  }
  .person {
    position: absolute;
    left: 40px;
    top: 60px;
  }
  .person-name { font-size: 40px; font-weight: 400; line-height: 1.1; }
  .person-title { font-size: 20px; margin-top: 4px; }
  .person-links {
    position: absolute;
    left: 40px;
    top: 185px;
    font-size: 19px;
    line-height: 1.45;
  }
  .person-links .web { font-size: 16px; }
  .office {
    position: absolute;
    right: 50px;
    top: 30px;
    text-align: right;
    font-size: 21px;
    line-height: 1.35;
  }
  .office .phones { margin-top: 14px; }
</style>
</head>
<body>
  <main class="card">
    <div class="world-map" role="img" aria-label="Dark world map in the card background"></div>
    <div class="brand-name">Tallow Crest</div>
    <div class="brand-web">www.tallowcrest.com</div>
    <section class="contact-panel">
      <div class="person">
        <div class="person-name">Mara Linden</div>
        <div class="person-title">CEO</div>
      </div>
      <div class="person-links">
        <div class="email">mara@tallowcrest.com</div>
        <div class="web">www.tallowcrest.com</div>
      </div>
      <div class="office">
        <div>480 N Harbor Lane</div>
        <div>Brookfield, State 2040</div>
        <div class="phones">1.555.20417<br>1.555.20418</div>
      </div>
    </section>
  </main>
</body>
</html>
```